Back Pain

Need a flyer similar to the attached draft. This is to be handed out to prospective patients. Note that Sketch Hive has already designed the logo. If you need a copy please contact me

```html
<!DOCTYPE html>
<html lang="en">
<head>
<meta charset="utf-8">
<title>Spine Ease Clinic – Flyer</title>
<link href="https://fonts.googleapis.com/css2?family=Oswald:wght@300;400;500;600;700&family=Montserrat:wght@400;500;600;700;800&display=swap" rel="stylesheet">
<style>
  :root{
    --green:#7cc242;
    --green-mid:#4fa86a;
    --teal:#2e8f8a;
    --blue:#0a6fbe;
    --ink:#222222;
    --grey-bar:#c6c7c8;
    --grey-dark:#555759;
    --bg:#f1f2f2;
    --white:#ffffff;
  }
  *{margin:0;padding:0;box-sizing:border-box}
  html,body{width:849px;height:1200px;overflow:hidden;background:var(--bg)}
  .flyer{position:relative;width:849px;height:1200px;overflow:hidden;
    background:radial-gradient(ellipse at 30% 55%, #ffffff 0%, #f4f5f5 55%, #e9eaea 100%);
    font-family:'Montserrat',sans-serif;color:var(--ink)}
  .backdrop{position:absolute;left:0;top:0}
  .abs{position:absolute}

  /* brand */
  .brand{left:34px;top:38px;width:266px;text-align:center}
  .brand-mark{width:92px;height:92px;border-radius:50%;background:var(--teal);margin:0 auto 12px}
  .brand-name{font-family:'Montserrat',sans-serif;font-weight:700;font-size:20px;color:var(--blue);letter-spacing:-.3px;line-height:1;white-space:nowrap}
  .brand-sub{font-family:'Montserrat',sans-serif;font-weight:700;font-size:9.5px;color:var(--blue);letter-spacing:2px;margin-top:4px;white-space:nowrap}

  /* condition tags */
  .tag{position:absolute;height:27px;padding:0 8px;display:flex;align-items:center;justify-content:flex-end;
    font-family:'Oswald',sans-serif;font-weight:500;font-size:18px;color:var(--white);letter-spacing:.3px;white-space:nowrap;
    background:linear-gradient(90deg,var(--green-mid),var(--blue))}
  .tag.center{justify-content:center}

  /* headline */
  .headline{left:27px;top:468px;font-family:'Oswald',sans-serif;font-weight:700;font-size:41px;line-height:42px;
    letter-spacing:-.5px;color:var(--teal);white-space:nowrap;
    background:linear-gradient(90deg,var(--green-mid),var(--teal) 50%,var(--blue));
    -webkit-background-clip:text;background-clip:text;-webkit-text-fill-color:transparent}

  /* chart */
  .axis-title{left:22px;top:790px;transform:rotate(-90deg);transform-origin:left top;
    font-family:'Oswald',sans-serif;font-weight:500;font-size:16px;color:var(--grey-dark);letter-spacing:.5px;white-space:nowrap}
  .bar{position:absolute;width:46px;background:var(--grey-bar);display:flex;align-items:center;justify-content:center;
    font-family:'Montserrat',sans-serif;font-weight:600;font-size:17px;color:var(--ink)}
  .baseline{left:63px;top:789px;width:318px;height:2px;background:linear-gradient(90deg,var(--green-mid),var(--blue))}
  .tick{position:absolute;top:798px;width:60px;text-align:center;font-weight:700;font-size:17px;color:var(--ink)}
  .x-title{left:33px;top:822px;font-size:18px;font-weight:400;letter-spacing:1.2px;color:var(--grey-dark);white-space:nowrap}
  .tilt-icon{left:295px;top:627px;width:102px;height:93px;border-radius:50% 50% 10px 40%;
    background:linear-gradient(160deg,var(--green-mid),var(--blue))}

  /* stat */
  .stat{left:430px;top:702px;width:270px;text-align:right;font-family:'Oswald',sans-serif;color:var(--grey-dark);white-space:nowrap}
  .stat-top{font-weight:600;font-size:19px;line-height:24px;letter-spacing:.2px}
  .stat-big{font-weight:700;font-size:28px;line-height:33px;letter-spacing:-.3px;color:var(--teal);
    background:linear-gradient(90deg,var(--green-mid),var(--teal));-webkit-background-clip:text;background-clip:text;-webkit-text-fill-color:transparent}
  .stat-bottom{font-weight:400;font-size:19px;line-height:22px;letter-spacing:.8px}
  .stat-pie{left:706px;top:682px}

  /* doctor & offer */
  .doctor{left:20px;top:872px;width:400px;text-align:center;white-space:nowrap}
  .doctor-name{font-family:'Oswald',sans-serif;font-weight:700;font-size:40px;line-height:44px;color:var(--teal);
    background:linear-gradient(90deg,var(--teal),var(--green-mid));-webkit-background-clip:text;background-clip:text;-webkit-text-fill-color:transparent}
  .doctor-loc{font-family:'Oswald',sans-serif;font-weight:300;font-size:23px;color:var(--ink);line-height:28px}
  .offer-badge{left:23px;top:955px;width:74px;height:74px;border-radius:50%;
    background:linear-gradient(135deg,var(--teal),var(--green-mid));color:var(--white);
    font-family:'Oswald',sans-serif;font-weight:700;font-size:36px;display:flex;align-items:center;justify-content:center;letter-spacing:-2px}
  .offer-badge small{font-size:13px;font-weight:400;letter-spacing:0;align-self:flex-start;margin-top:18px;margin-left:2px}
  .offer-title{left:103px;top:968px;font-family:'Oswald',sans-serif;font-weight:700;font-size:35px;line-height:44px;
    color:var(--green-mid);letter-spacing:-.5px;white-space:nowrap;
    background:linear-gradient(90deg,var(--teal),var(--green));-webkit-background-clip:text;background-clip:text;-webkit-text-fill-color:transparent}
  .offer-note{right:431px;top:1014px;text-align:right;font-family:'Oswald',sans-serif;font-weight:600;font-size:25px;line-height:30px;color:var(--ink);white-space:nowrap}
  .offer-url{right:431px;top:1042px;text-align:right;font-family:'Oswald',sans-serif;font-weight:400;font-size:26px;line-height:34px;color:var(--ink);letter-spacing:.6px;white-space:nowrap}

  /* promise box */
  .promise{left:436px;top:843px;width:388px;height:242px;border-radius:26px;
    background:linear-gradient(90deg,var(--teal),var(--green-mid) 60%,#6bb657);
    color:var(--white);text-align:center;display:flex;flex-direction:column;justify-content:center;
    font-size:24.5px;line-height:35px;font-weight:400;white-space:nowrap}
  .promise b{font-weight:800}

  /* footer */
  .contact{display:flex;align-items:center;gap:8px;font-size:14px;font-weight:600;color:var(--ink);white-space:nowrap}
  .contact.small{font-size:12.5px;font-weight:500}
  .contact svg{flex:none}
  .sign{left:626px;top:1110px;padding-left:10px;border-left:2px solid var(--blue);white-space:nowrap}
  .sign-name{font-weight:600;font-size:15px;color:var(--blue);line-height:18px}
  .sign-role{font-weight:500;font-size:10px;color:var(--blue)}
  .footer-band{left:0;top:1165px;width:849px;height:35px;background:linear-gradient(90deg,var(--green),var(--teal) 55%,var(--blue))}
</style>
</head>
<body>
<div class="flyer">

  <svg class="backdrop" width="849" height="1200" viewBox="0 0 849 1200">
    <defs>
      <linearGradient id="swoosh" x1="0" y1="0" x2="1" y2="0">
        <stop offset="0" stop-color="#0a6fbe"/>
        <stop offset="1" stop-color="#2e8f8a"/>
      </linearGradient>
      <linearGradient id="arcGreen" x1="0" y1="0" x2="1" y2="1">
        <stop offset="0" stop-color="#4fa86a"/>
        <stop offset="1" stop-color="#7cc242"/>
      </linearGradient>
      <radialGradient id="photoTone" cx="0.6" cy="0.55" r="0.6">
        <stop offset="0" stop-color="#ef9a80"/>
        <stop offset="0.45" stop-color="#d9b3a0"/>
        <stop offset="1" stop-color="#dcdedf"/>
      </radialGradient>
      <clipPath id="photoClip"><circle cx="590" cy="300" r="272"/></clipPath>
    </defs>
    <circle cx="600" cy="300" r="330" fill="#ffffff" opacity=".9"/>
    <path d="M375 40 C470 -20 640 -20 760 30 C820 60 849 90 849 100 L849 60 C800 10 690 -15 560 0 C480 8 420 25 375 40 Z" fill="url(#arcGreen)"/>
    <path d="M849 110 L849 440 C845 470 830 470 830 440 C840 340 820 220 780 150 C820 150 849 130 849 110 Z" fill="url(#arcGreen)" opacity=".9"/>
    <path d="M318 420 C270 300 300 150 400 80 C330 160 300 290 318 420 Z" fill="#0a6fbe"/>
    <g clip-path="url(#photoClip)">
      <rect x="300" y="20" width="560" height="560" fill="url(#photoTone)" role="img" aria-label="Photo of a man holding his lower back, with a glowing spine overlay showing pain points"/>
    </g>
    <path d="M455 535 C520 560 610 560 680 510 C640 530 620 470 700 470 C770 470 820 440 849 400 L849 470 C800 560 700 610 600 600 C540 595 490 570 455 535 Z" fill="url(#swoosh)"/>
  </svg>

  <div class="abs brand">
    <div class="brand-mark"></div>
    <div class="brand-name">SPINE EASE CLINIC</div>
    <div class="brand-sub">DR OWEN HARPER - CHIROPRACTOR</div>
  </div>

  <svg class="abs" style="left:0;top:0" width="849" height="450" viewBox="0 0 849 450">
    <g stroke="#7cc242" stroke-width="2" fill="none">
      <path d="M426 63 V46 H504"/>
      <path d="M497 92 V79 H523"/>
      <path d="M600 110 H679"/>
      <path d="M644 207 H722"/>
      <path d="M627 418 H702"/>
    </g>
    <path d="M742 272 V328" stroke="#2e8f8a" stroke-width="2"/>
  </svg>

  <div class="tag center" style="left:504px;top:32px;width:111px">HEADACHES</div>
  <div class="tag center" style="left:523px;top:66px;width:111px">NECK PAIN</div>
  <div class="tag" style="left:679px;top:97px;width:145px">SHOULDER PAIN</div>
  <div class="tag" style="left:722px;top:193px;width:102px">BACK PAIN</div>
  <div class="tag" style="left:663px;top:246px;width:161px">ARM &amp; HAND PAIN</div>
  <div class="tag center" style="left:702px;top:405px;width:122px">SCIATICA</div>

  <h1 class="abs headline">AS THE HEAD TILTS<br>FORWARD. MORE FORCE<br>IS PLACED ON THE SINE</h1>

  <div class="abs axis-title">PRESSURE ON SPINE (LBS)</div>
  <div class="bar" style="left:63px;top:614px;height:176px">60</div>
  <div class="bar" style="left:132px;top:648px;height:142px;padding-top:12px">49</div>
  <div class="bar" style="left:201px;top:675px;height:115px;padding-top:16px">40</div>
  <div class="bar" style="left:269px;top:713px;height:77px;padding-top:16px">27</div>
  <div class="bar" style="left:335px;top:763px;height:27px">12</div>
  <div class="abs baseline"></div>
  <div class="tick" style="left:56px">60°</div>
  <div class="tick" style="left:125px">45°</div>
  <div class="tick" style="left:194px">30°</div>
  <div class="tick" style="left:262px">15°</div>
  <div class="tick" style="left:331px">0°</div>
  <div class="abs x-title">DEGREES OF FORWARD HEAT TILT</div>
  <div class="abs tilt-icon" role="img" aria-label="Icon of a head bent forward with neck pain sparks"></div>

  <div class="abs stat">
    <div class="stat-top">THE AVERAGE PERSON SPENDS</div>
    <div class="stat-big">8-11 HOURS PER DAY</div>
    <div class="stat-bottom">USING ELECTRONIC DEVICES</div>
  </div>
  <svg class="abs stat-pie" width="118" height="118" viewBox="0 0 118 118">
    <circle cx="59" cy="59" r="58" fill="#555759"/>
    <path d="M59 59 L59 1 A58 58 0 0 1 105 94 Z" fill="#3b9a80"/>
  </svg>

  <div class="abs doctor">
    <div class="doctor-name">DR. OWEN HARPER</div>
    <div class="doctor-loc">Now in Westhaven At: 42 Harbour Rd.</div>
  </div>

  <div class="abs offer-badge">50<small>%</small></div>
  <div class="abs offer-title">INITIAL CONSULTATION</div>
  <div class="abs offer-note">If you book on limit at:</div>
  <div class="abs offer-url">www.spineeaseclinic.com.au</div>

  <div class="abs promise">
    <div><b>SPINE EASE CLINIC</b></div>
    <div>CAN HELP CORRECT AND</div>
    <div>PREVENT THESE PROBLEMS</div>
    <div>BY <b>RESTORING</b> AND</div>
    <div><b>MAINTAINING PROPER</b></div>
    <div><b>ALIGNMENT</b> OF THE <b>NECK</b></div>
  </div>

  <div class="abs contact" style="left:34px;top:1114px">
    <svg width="20" height="20" viewBox="0 0 20 20"><circle cx="10" cy="10" r="10" fill="var(--blue)"/><path d="M7 5 l2 2.5 -1.2 1.5 c.8 1.6 1.8 2.6 3.2 3.3 l1.5 -1.2 2.5 2 -1 1.7 c-4 0 -8 -4 -8.5 -8.3 z" fill="#fff"/></svg>
    <span>0400 555 018</span>
  </div>
  <div class="abs contact small" style="left:34px;top:1137px">
    <svg width="20" height="20" viewBox="0 0 20 20"><circle cx="10" cy="10" r="10" fill="var(--blue)"/><path d="M10 4 a4 4 0 0 1 4 4 c0 3 -4 7.5 -4 7.5 s-4 -4.5 -4 -7.5 a4 4 0 0 1 4 -4 z" fill="#fff"/><circle cx="10" cy="8" r="1.5" fill="var(--blue)"/></svg>
    <span>Unit 12/7 Marlow St, Northbay WA 6001</span>
  </div>
  <div class="abs contact small" style="left:346px;top:1114px">
    <svg width="20" height="20" viewBox="0 0 20 20"><circle cx="10" cy="10" r="10" fill="var(--blue)"/><rect x="5" y="6.5" width="10" height="7" fill="none" stroke="#fff" stroke-width="1.3"/><path d="M5 6.5 l5 4 5 -4" fill="none" stroke="#fff" stroke-width="1.3"/></svg>
    <span>owen@spineeaseclinic.com.au</span>
  </div>
  <div class="abs contact small" style="left:346px;top:1137px">
    <svg width="20" height="20" viewBox="0 0 20 20"><circle cx="10" cy="10" r="10" fill="var(--blue)"/><circle cx="10" cy="10" r="5.5" fill="none" stroke="#fff" stroke-width="1.2"/><path d="M4.5 10 h11 M10 4.5 c-2.5 3 -2.5 8 0 11 M10 4.5 c2.5 3 2.5 8 0 11" fill="none" stroke="#fff" stroke-width="1"/></svg>
    <span>www.spineeaseclinic.com.au</span>
  </div>
  <div class="abs sign">
    <div class="sign-name">DR. OWEN HARPER</div>
    <div class="sign-role">CHIROPRACTOR</div>
  </div>

  <div class="abs footer-band"></div>
</div>
</body>
</html>
```